Client Publishing Agency Brochure

We need a company brochure for a new company based in Cape Town, South Africa called Velvet Harbour Studios (VHS).

We need a brochure marketing our publishing agency (vhs:inkwell) and our creative, interactive & print production division (vhs:forge). Develop a fresh design concept which will direct the design of our new website in the near future. (So don't pay attention to our current web page. It does not reflect our brand).

vhs:inkwell is a content marketing agency offering our clients (B2B, B2C, NPO, Professional & Membership Organizations) branded publishing to build trust, authority and relationships with their customers. A typical content strategy may include communication through client print or online magazine, newsletters, microsite, website, social technology and plenty more). We want to communicate that company's need to change their mind set from promoting their products and begin to invest in developing a relationship with their potential & existing customers. The drive is a Return On Objectives (business & marketing objectives) and interest is a Return On Investment (ROI).

vhs:forge is a creative, interactive & print production agency which supports our client's marketing collateral needs.
Updates

Hi Designers,

This is a response to questions posted earlier to assist you in your project.

Q.What will the size of brochure be?
A. A4 size with folder flap for the back cover

Q.Will it be a three panels double sided?
A. Depends on your creative concept. But if you make a 3 panel dbl side then layout two version for print (double sided 3 panel) and digital pdf (single pdf pages in sequence).

Q.The images that you supplied I know are just samples, What type of images are 
required? 
A. Depends on your creative concept. Let the style of the logo inspire you. What I liked in the examples is the classic, premium, quality feel. So no business stock imagery. I'm also a creative agency so that message needs to come through. Illustrated styles are welcome.

Q.Should design have same feel as your website? 
A. No. Our website is pending the outcome of the brochure. The brochure will be our creative direction for our new website. So creative an inspiring and clean brochure.

Please feel free to post additional questions. Good Luck and thank you for your participation.

Project Deadline Extended
Reason: The designers have not produced a style and concept that reflects our brand. Would like to guide them more to reach the right look for our company.

Hi Designers...

I have not been happy with the quality of ideas and execution of those ideas. This I understand could a combination of a poor brief and a non-guarenteed project.

I have rectified the brief and have guaranteed the award. Please don't hold back on your creativity and return the guarantee for high quality.

Please ask me any questions to better understand what we are looking for.

Remember. This brochure is a new design concept. Do not visit the web page for inspiration. The new design concept for the brochure will set the tone and inspire a new website.

Lets create a beautiful product together.

Thank you for your participation.

Project Deadline Extended
Reason: Designers are not following the brief, and not respecting the logo and colour policies/guidelines and those who are submitting work are not asking questions throughout the process to get a better understanding of what we need. All design submissions are always at the last minute. And some designers are are not real designers and using web development software to produce print designs. More importantly after taking time to advise designers of changes, no effort is made by designers to make changes. Each designer submits 1 idea and think that they are going to win the lottery. Where is the work ethic and quality of service? Where are the submissions from the designers who accepted the participation fee? There were a few designers who promised participation and never showed up. Maybe it all our fault? But we not happy with the service and level of creativity. Not sure if these designers are taking pride in their work or not. I know a few of you are.

Target Market(s)

B2B, B2C, NPO, Professional & Membership Organizations - Make up professionals and decision makers across sectors from Shipping and Logistics, Manufacturing, Legal to Art & Culture.

Industry/Entity Type

Communication

Requirements
Must have
• Size: A4
x 2 Panels
+ Folder flap (for A4 Paper, business card slot)
Styled map to our premises. See map attachment for example.

Pages: 10 including cover (if you need more than this let your design motivate the need for more pages)

(See logo use eps file)
(See colour use eps file)

Nice to have
• Styled map to our premises. See attachment for example.
Should not have
• Do not take any inspiration from our website. It is just a free template to show customers that it is still under construction.

Do not include stock symbols and typical business stock images. Remember we are a creative offering, so our brochure should show originality, innovation and individuality.

```html
<!DOCTYPE html>
<html lang="en">
<head>
<meta charset="utf-8">
<title>VHS Brochure – Member Magazine / Digital Sounds</title>
<link href="https://fonts.googleapis.com/css2?family=Source+Sans+3:wght@400;600;800&display=swap" rel="stylesheet">
<style>
  :root {
    --page-light: #c4c5c8;
    --page-mid: #b3b4b7;
    --page-dark: #9d9ea2;
    --ink: #1b1b1b;
    --black: #000000;
    --white: #ffffff;
    --rule: #3a3a3a;
    --wave-deep: #12207a;
    --wave-bright: #2d48d8;
    --sheet-red: #d21f45;
    --sheet-silver: #d9d9dc;
    --swatch-a: #e8423a;
    --swatch-b: #4ab3e8;
  }
  * { margin: 0; padding: 0; box-sizing: border-box; }
  html, body { width: 1200px; height: 849px; overflow: hidden; background: var(--page-mid); }
  body { font-family: "Source Sans 3", "Myriad Pro", Arial, sans-serif; color: var(--ink); position: relative; }

  .spread { position: absolute; inset: 0; }
  .page { position: absolute; top: 0; height: 849px; overflow: hidden; }
  .page--left {
    left: 0; width: 597px;
    background: radial-gradient(ellipse at 65% 35%, var(--page-light) 0%, var(--page-mid) 55%, var(--page-dark) 100%);
  }
  .page--right {
    left: 597px; width: 603px;
    background: radial-gradient(ellipse at 40% 30%, var(--page-light) 0%, var(--page-mid) 55%, var(--page-dark) 100%);
    border-left: 1px solid #a8a9ac;
  }

  .brand {
    position: absolute; top: 82px;
    display: flex; align-items: center; gap: 8px;
    font-weight: 800; font-size: 40px; letter-spacing: 1px; color: var(--black); line-height: 1;
  }
  .brand__mark { width: 14px; height: 14px; background: var(--black); }
  .page--left .brand { left: 58px; }
  .page--right .brand { left: 56px; }

  .section-tab {
    position: absolute; top: 74px; width: 148px; height: 54px;
    background: var(--black); color: var(--white);
    font-size: 14.5px; font-weight: 400;
    display: flex; align-items: center; justify-content: center;
  }
  .section-rule { position: absolute; top: 127px; left: 213px; width: 176px; height: 1px; background: var(--rule); }
  .section-tab { left: 388px; }

  .copy { position: absolute; top: 167px; font-size: 11.7px; line-height: 21.6px; z-index: 2; }
  .copy p + p { margin-top: 21.6px; }
  .page--left .copy { left: 55px; width: 405px; }
  .page--right .copy { left: 56px; width: 400px; }

  .sources { list-style: none; margin-bottom: 21.6px; }
  .sources li { display: flex; }
  .sources li + li { margin-top: 21.6px; }
  .sources__num { width: 36px; flex: none; }

  .art { position: absolute; z-index: 1; }
  .art--sheets-top {
    left: 468px; top: 420px; width: 118px; height: 145px;
    background: linear-gradient(135deg, var(--sheet-red) 0%, var(--sheet-red) 35%, var(--sheet-silver) 60%, #f2f2f3 100%);
  }
  .art--sheets-bottom {
    left: 255px; top: 624px; width: 305px; height: 148px;
    background: linear-gradient(120deg, #9a9a9e 0%, #ececee 45%, #8f8f93 100%);
  }
  .art--soundwave {
    left: 0; top: 618px; width: 603px; height: 156px;
    background: linear-gradient(180deg, rgba(45,72,216,0) 0%, var(--wave-deep) 20%, var(--wave-bright) 48%, #e8ecff 50%, var(--wave-bright) 52%, var(--wave-deep) 80%, rgba(18,32,122,0) 100%);
  }

  .swatch-strip {
    position: absolute; top: 779px; width: 290px; height: 22px;
    background: linear-gradient(90deg, var(--swatch-a), #f0c43a, #53b84a, var(--swatch-b), #c43aa0);
    opacity: .75;
  }
  .page--left .swatch-strip { left: 72px; }
  .page--right .swatch-strip { left: 245px; }

  .folio {
    position: absolute; top: 783px; width: 16px; height: 16px;
    background: var(--black); color: var(--white);
    font-size: 9px; font-weight: 600; display: flex; align-items: center; justify-content: center;
  }
  .page--left .folio { left: 57px; }
  .page--right .folio { left: 521px; }
</style>
</head>
<body>
<main class="spread">
  <section class="page page--left">
    <div class="brand"><span>VHS</span><span class="brand__mark"></span></div>
    <div class="section-rule"></div>
    <h2 class="section-tab">Member Magazine</h2>

    <div class="copy">
      <p>Financial pressures on all business forms show no signs of slowing down present challenges to delivering the customer promise. Professional and member based organizations are no exception to the rule have unique challenges ranging from subscription fees, commercial activities, through to increasing competition of independent professional services and the surge of freely accessible e-social networks, and the list is extensive.</p>
      <p>As a member organization you must innovate traditional marketing strategies by investing in authentic consistent engagement strategies to attract and retain customers. A clear, cohesive, professional voice will reinforce the values shared and drive business interest. Your members will be proud to read, contribute and share their magazine experiences with their extended networks, illuminating the value received from being apart of your community. The result is a trusted voice within your industry.</p>
      <p>Our team produces the highest quality content on print and digital media and adopts the professional values subscribed to by your organization.</p>
      <p>Our commercial services offer an opportunity of leveraging off advertising and sponsorship, considerably reducing project costs while helping your business audience increase marketing effectiveness.</p>
    </div>

    <div class="art art--sheets-top" role="img" aria-label="Curling red and silver paper sheets illustration"></div>
    <div class="art art--sheets-bottom" role="img" aria-label="Scattered silver paper sheets illustration"></div>

    <div class="swatch-strip" role="img" aria-label="Row of small coloured squares"></div>
    <div class="folio">5</div>
  </section>

  <section class="page page--right">
    <div class="brand"><span>VHS</span><span class="brand__mark"></span></div>
    <div class="section-rule"></div>
    <h2 class="section-tab">Digital Sounds</h2>

    <div class="copy">
      <p>Three separate research sources reveal more than 50% of magazine readers want digital content but not at the expense of print.<br>Sources:</p>
      <ol class="sources">
        <li><span class="sources__num">1.</span><span>Fold Street Media, 2010, finds amoung current subscribers, 53% chose to renew with a digital product.</span></li>
        <li><span class="sources__num">2.</span><span>Brand Leaders Forum, 2010, finds 87% of those interested in reading magazines on a digital device still want a printed copy.</span></li>
        <li><span class="sources__num">3.</span><span>Larkfield Group/Orrin/Quillmark Research, 2010, finds 75% of consumers feel that digital content complements print, yet 25% fell it replaces print.</span></li>
      </ol>
      <p>Therefore our digital approach is creating creative, engaging and cost- effective scalable compliments to print through HTML, PDF, or microsites.</p>
      <p>Organic SEO principals drive our content engineering style ensuring online visibility, experience and tracking capabilities while your e-publication promises contagious interactive engagement through a host of features. Features include personalization, graphic artistry, video and rich media, analytics and social media linkage. The result is an interactive communication campaign limitless in engagement capacity in any media wherever your audience might be.</p>
    </div>

    <div class="art art--soundwave" role="img" aria-label="Glowing blue sound wave illustration"></div>

    <div class="swatch-strip" role="img" aria-label="Row of small coloured squares"></div>
    <div class="folio">6</div>
  </section>
</main>
</body>
</html>
```